Brisk Meadow Builders needs an updated flyer

Instructions are in a .pdf called "Instructions. All photos and logos are included along with the original flyer in .ai

We are looking for a fresh design that promotes sustainability.

```html
<!DOCTYPE html>
<html lang="en">
<head>
<meta charset="utf-8">
<title>Brisk Meadow Builders – Meadow Gable Mini Flyer</title>
<link rel="stylesheet" href="https://fonts.googleapis.com/css2?family=Montserrat:wght@200;400;500;600;700;800&family=Archivo:wght@700;800&display=swap">
<style>
  :root{
    --ink:#1e1e1e;
    --dark:#202020;
    --green:#5fa246;
    --orange:#f0a93b;
    --white:#ffffff;
    --mist:#e3e4e8;
    --mist-deep:#cfd2d8;
    --sky:#9dbfd6;
  }
  *{margin:0;padding:0;box-sizing:border-box}
  html,body{width:928px;height:1200px;overflow:hidden;background:var(--white)}
  body{font-family:"Montserrat",sans-serif;color:var(--ink)}
  .flyer{position:relative;width:928px;height:1200px;overflow:hidden;background:var(--white)}
  .abs{position:absolute}

  .tagline{left:0;top:22px;width:928px;text-align:center;font-weight:700;font-size:14.5px;letter-spacing:.6px}

  .hero-photo{left:0;top:62px;width:457px;height:372px;
    background:linear-gradient(180deg,var(--sky) 0%,#cfe0ea 30%,#5f7f4a 55%,#6d6f72 80%,#4f5154 100%)}

  .title-panel{left:457px;top:62px;width:471px;height:340px;background:var(--dark);color:var(--white)}
  .brand{right:40px;top:96px;display:flex;align-items:center;gap:8px;font-weight:700;font-size:17px;letter-spacing:.4px;color:var(--white)}
  .brand-square{width:14px;height:14px;background:var(--white)}
  .title-the{left:553px;top:150px;font-weight:200;font-size:60px;line-height:1;color:var(--white)}
  .title-quote{left:497px;top:202px;font-family:"Archivo",sans-serif;font-weight:800;font-size:80px;line-height:1;color:var(--white)}
  .title-name{left:552px;top:228px;font-family:"Archivo",sans-serif;font-weight:800;font-size:45px;line-height:53px;color:var(--white)}
  .title-sub{left:552px;top:342px;font-weight:700;font-size:16px;color:var(--white)}

  .features{left:0;top:434px;width:928px;height:263px;background:var(--green)}

  .price-bar{z-index:2;left:457px;top:402px;width:471px;height:61px;background:var(--orange);color:var(--white);display:flex;align-items:center}
  .price-label{width:213px;text-align:right;font-size:12.5px;line-height:16px;letter-spacing:.4px;font-weight:500}
  .price-value{margin-left:16px;font-weight:800;font-size:37px;line-height:1;white-space:nowrap}

  .features-title{left:56px;top:452px;font-weight:500;font-size:36px;color:var(--white)}
  .feature-list{list-style:none;color:var(--white);font-size:13.4px;line-height:18px;letter-spacing:.2px}
  .feature-list li{position:relative;padding-left:32px;margin-bottom:13px}
  .feature-list svg{position:absolute;left:0;top:-4px;width:24px;height:24px}
  .features-left{left:58px;top:513px;width:395px}
  .features-right{left:505px;top:508px;width:410px}
  .features-right li{margin-bottom:15px}

  .guide-line{z-index:1;background:var(--white)}

  .gallery-photo{top:703px;height:167px;background:linear-gradient(180deg,#6f8f58 0%,#e9ecef 40%,#f4f4f4 65%,#5d5f63 100%)}

  .options{left:0;top:870px;width:441px;height:225px;background:linear-gradient(90deg,var(--mist-deep),var(--mist))}
  .section-head{font-weight:800;font-size:22px;color:var(--green);letter-spacing:.5px}
  .options-head{left:44px;top:897px}
  .options-list{left:44px;top:930px;list-style:none;font-size:14.3px;line-height:21.3px;font-weight:500}
  .options-list li::before{content:"• "}
  .uses-head{left:470px;top:897px}
  .uses{left:471px;top:929px;width:430px;font-size:16.8px;line-height:22.5px;font-weight:400}
  .uses p{margin-bottom:5px}
  .uses b{font-weight:800}

  .footer{left:0;top:1095px;width:928px;height:105px;background:var(--dark);color:var(--white);text-align:center}
  .footer-note{padding-top:23px;font-size:13px}
  .footer-contact{margin-top:12px;font-size:22px;font-weight:500;letter-spacing:.5px}
  .footer-contact .web{color:var(--orange)}
  .footer-contact .sep{margin:0 10px}
</style>
</head>
<body>
<main class="flyer">
  <svg width="0" height="0" style="position:absolute">
    <symbol id="tick" viewBox="0 0 24 24">
      <rect x="2" y="5" width="16" height="16" fill="none" stroke="#fff" stroke-width="2"/>
      <path d="M6 13l4 4L22 3" fill="none" stroke="#fff" stroke-width="3" stroke-linecap="round" stroke-linejoin="round"/>
    </symbol>
  </svg>

  <p class="abs tagline">A SUSTAINABLE SOLUTION TO MOBILE VENDING WITH AN ICONIC FARM HOUSE ARCHITECTURE</p>

  <div class="abs hero-photo" role="img" aria-label="Photo of a white farmhouse-style vending trailer with solar roof and wooden porch deck, parked on a paved lot among trees"></div>

  <section class="abs title-panel" aria-label="Product title"></section>
  <div class="abs brand"><span class="brand-square"></span>BRISK MEADOW BUILDERS</div>
  <div class="abs title-the">The</div>
  <div class="abs title-quote">“</div>
  <h1 class="abs title-name">Meadow Gable<br>Mini”</h1>
  <p class="abs title-sub">Luxury, mobile vending house</p>

  <section class="abs features" aria-label="Base unit features"></section>

  <div class="abs price-bar">
    <span class="price-label">BASE PRICE<br>STARTING AT JUST</span>
    <span class="price-value">$65,000</span>
  </div>

  <h2 class="abs features-title">Base unit features:</h2>
  <ul class="abs feature-list features-left">
    <li><svg><use href="#tick"/></svg>Trailer features tandem wheels w/ brakes.</li>
    <li><svg><use href="#tick"/></svg>Steel frame construction for fire retardation safety and weight reduction.</li>
    <li><svg><use href="#tick"/></svg>100% Off grid with solar &amp; up to 20 KWH’s of lithium battery storage allowing trailer to be used in places not accessible by traditional trailers.</li>
    <li><svg><use href="#tick"/></svg>60 Gallon water supply tank</li>
  </ul>
  <ul class="abs feature-list features-right">
    <li><svg><use href="#tick"/></svg>70 Gallon waste water tank.</li>
    <li><svg><use href="#tick"/></svg>Cupboards, cabinets &amp; four stainless steel sinks.</li>
    <li><svg><use href="#tick"/></svg>60” Gas shock serving window.</li>
    <li><svg><use href="#tick"/></svg>Custom interiors to suit various uses</li>
    <li><svg><use href="#tick"/></svg>Multiple sizes from 12’, 16’, 20’ &amp; 24’ long</li>
  </ul>

  <div class="abs guide-line" style="left:44px;top:307px;width:96px;height:1px"></div>
  <div class="abs guide-line" style="left:44px;top:307px;width:1px;height:390px"></div>

  <div class="abs gallery-photo" style="left:0;width:298px" role="img" aria-label="Vending trailer seen from the front corner with open serving window"></div>
  <div class="abs gallery-photo" style="left:305px;width:313px" role="img" aria-label="Side view of the vending trailer with serving window and solar panels"></div>
  <div class="abs gallery-photo" style="left:624px;width:304px" role="img" aria-label="Vending trailer from the rear corner showing door and porch deck"></div>

  <section class="abs options" aria-label="Available options"></section>
  <h2 class="abs section-head options-head">AVAILABLE OPTIONS:</h2>
  <ul class="abs options-list">
    <li>HVAC - Nordair Mini Split</li>
    <li>Cooler / Glass front Commercial refrigerator</li>
    <li>Upper loft storage area</li>
    <li>Signage and graphics</li>
    <li>Ice machine</li>
    <li>3 foot fold down porch deck</li>
  </ul>

  <h2 class="abs section-head uses-head">USE CASES:</h2>
  <div class="abs uses">
    <p><b>Food:</b> Lemonade, Coffee, Pizza, Ccookies, Doughnuts, Farm to table etc.</p>
    <p><b>Retail:</b> Clothing, watches, jewelry, flowers.</p>
    <p><b>Corporate:</b> Grocery / convenience, clothing, watches, jewelry, flowers, crafts, art.</p>
    <p><b>Fundraisers:</b> Boy/Girl sports, non profits</p>
  </div>

  <footer class="abs footer">
    <p class="footer-note">Need a custom branded solution for your business? Let’s talk!”</p>
    <p class="footer-contact"><span>(705) 555-0148</span><span class="sep">|</span><span class="web">www.BriskMeadowBuilders.com</span></p>
  </footer>
</main>
</body>
</html>
```